Dane Calloway Photography

Would like the Business card to have a cool logo. I’m targeting wedding/ engagement: portrait photography. My phone number on it. And my business email address.

Target Market(s)

Wedding/portrait/engagement photography.

```html
<!DOCTYPE html>
<html lang="en">
<head>
<meta charset="utf-8">
<title>Dane Calloway Photography — Business Card</title>
<link href="https://fonts.googleapis.com/css2?family=Montserrat:wght@300;400&display=swap" rel="stylesheet">
<style>
  :root {
    --canvas-bg: #d9d6d2;
    --card-front: #ecdfdb;
    --card-back: #ebebea;
    --accent-circle: #ecd4d6;
    --ink: #3b3536;
    --ink-soft: #4a4445;
  }
  * { box-sizing: border-box; margin: 0; padding: 0; }
  html, body {
    width: 1200px;
    height: 960px;
    overflow: hidden;
    background: var(--canvas-bg);
    font-family: "Montserrat", sans-serif;
    color: var(--ink);
  }
  .card-set {
    width: 1200px;
    height: 960px;
    display: flex;
    flex-direction: column;
    align-items: center;
    justify-content: center;
    gap: 48px;
  }
  .card {
    width: 588px;
    height: 336px;
    position: relative;
    box-shadow: 0 6px 18px rgba(0,0,0,0.12);
  }
  .card--front { background: var(--card-front); }
  .card--back { background: var(--card-back); }

  .wordmark {
    position: absolute;
    left: 50%;
    top: 50%;
    transform: translate(-50%, -50%);
    text-align: center;
    font-weight: 300;
    color: var(--ink);
    white-space: nowrap;
  }
  .wordmark__name {
    display: block;
    font-size: 34px;
    letter-spacing: 0.04em;
  }
  .wordmark__line {
    display: block;
    margin-top: 8px;
    font-size: 12px;
    letter-spacing: 0.42em;
  }

  .back-logo {
    position: absolute;
    left: 50%;
    top: 110px;
    transform: translateX(-50%);
    display: flex;
    align-items: center;
    gap: 16px;
  }
  .back-logo__circle {
    width: 74px;
    height: 74px;
    border-radius: 50%;
    background: var(--accent-circle);
    flex: none;
  }
  .back-logo .wordmark {
    position: static;
    transform: none;
    text-align: left;
  }
  .back-logo .wordmark__name { font-size: 28px; }
  .back-logo .wordmark__line { font-size: 10px; margin-top: 6px; }

  .services {
    position: absolute;
    left: 0;
    right: 0;
    top: 210px;
    text-align: center;
    font-size: 10px;
    font-weight: 400;
    letter-spacing: 0.38em;
    color: var(--ink-soft);
  }
  .services span + span { margin-left: 18px; }

  .contact {
    position: absolute;
    left: 0;
    right: 0;
    top: 238px;
    text-align: center;
    font-size: 10.5px;
    font-weight: 400;
    letter-spacing: 0.06em;
    line-height: 1.6;
    color: var(--ink-soft);
  }
</style>
</head>
<body>
  <main class="card-set">
    <section class="card card--front" aria-label="Business card front">
      <div class="wordmark">
        <span class="wordmark__name">Dane Calloway</span>
        <span class="wordmark__line">PHOTOGRAPHY</span>
      </div>
    </section>

    <section class="card card--back" aria-label="Business card back">
      <div class="back-logo">
        <span class="back-logo__circle"></span>
        <div class="wordmark">
          <span class="wordmark__name">Dane Calloway</span>
          <span class="wordmark__line">PHOTOGRAPHY</span>
        </div>
      </div>
      <p class="services"><span>WEDDING</span><span>PORTRAIT</span><span>LIFESTYLE</span></p>
      <p class="contact">
        555 014 2398<br>
        hello@danecalloway.com
      </p>
    </section>
  </main>
</body>
</html>
```